Website design for Cloud Scheduling Company

We have a design build that is based on a corporate template. the structure and content is there but the design does not match the 'feel' of what we are going for from a design perspective.
http://plumvexa.com/demo/ferret/

please follow this structure for the site layout but add new ideas also.

Scheduling is boring and typically a serious topic, with our new logo we are looking to bring a quirky, fun feeling to what our site does.

It is a powerful scheduling platform that is used mainly in Volunteer environments and we want our brand to reflect this.

A lot of sites use images of real people in photographs but i would like to see us use more vector graphics and illustrations in the design so it is a bit more exciting.

The homepage should have a large screen capture of the app on different devices (large monitor, tablet, and smartphone) which is pretty standard for this type of website.i have attached a jpeg where you can get images from as well as the logo so you can get a sense of the look and feel.

this is what I envision being the image in the main banner as it showcases the application https://www.zorbimo.ca/search?q=responsive&biw=1920&bih=920&source=lnms&tbm=isch&sa=X&ved=0ahUKEwiAlqahjv_KAhXrlIMKHToqB5oQ_AUIBigB#imgrc=a75LOlLuwcKyqM%3A

Again, what I need for this project is a design for the site at http://plumvexa.com/demo/ferret/. it is already coded but i need a netter design. focus on homepage, pricing page and a general subpage please.

Target Market(s)

Volunteer organization Administrators

Industry/Entity Type

It Company

Number of Pages Required

3 page

Font styles to use
Sans Serif

Colors
0355a3
f37122

Requirements
Nice to have
• use graphics instead of photographs. you can include some photos but i want the look and feel to be consistent with the playfulness of the logo so the site isnt too serious. The site still has to be professional.

```html
<!DOCTYPE html>
<html lang="en">
<head>
<meta charset="utf-8">
<title>tallyroost – Choose Your Plan</title>
<link href="https://fonts.googleapis.com/css2?family=Open+Sans:wght@400;600;700&family=Raleway:wght@400;500;600;700;800&display=swap" rel="stylesheet">
<style>
:root{
  --blue:#0355a3;
  --blue-title:#0d5aa7;
  --blue-top-a:#1c5cab;
  --blue-top-b:#3d7fc9;
  --orange:#f7941d;
  --orange-btn:#f37122;
  --dark:#333c48;
  --footer:#0b4f96;
  --footer-base:#09438a;
  --text:#555;
  --row-alt:#f5f5f5;
  --line:#e3e3e3;
  --white:#fff;
}
*{box-sizing:border-box;margin:0;padding:0}
html,body{width:1200px;height:1131px;overflow:hidden}
body{position:relative;background:var(--white);font-family:"Open Sans",sans-serif;color:var(--text)}
.topbar{position:absolute;left:0;top:0;width:1200px;height:31px;background:linear-gradient(90deg,var(--blue-top-a),var(--blue-top-b) 60%,var(--blue-top-a));color:var(--white);font-size:9px;font-weight:700}
.topbar .contact{position:absolute;left:88px;top:0;height:31px;display:flex;align-items:center;gap:8px}
.topbar .contact span{display:flex;align-items:center;gap:5px}
.socials{display:flex;gap:12px;align-items:center}
.topbar .socials{position:absolute;right:90px;top:9px}
.dot{width:13px;height:13px;border-radius:50%;background:var(--white);opacity:.9}
.navbar{position:absolute;left:0;top:31px;width:1200px;height:70px;background:var(--white);box-shadow:0 2px 3px rgba(0,0,0,.08)}
.brand{position:absolute;left:88px;top:18px;display:flex;align-items:center;gap:8px}
.brand-mark{width:30px;height:30px;border-radius:50%;background:var(--blue)}
.brand-name{font-family:"Raleway",sans-serif;font-weight:800;font-size:25px;color:var(--orange-btn);letter-spacing:-.3px}
.menu{position:absolute;left:404px;top:0;height:70px;display:flex;align-items:center;gap:27px;list-style:none}
.menu li{font-family:"Open Sans",sans-serif;font-size:13px;color:#1d5ea8}
.search{position:absolute;left:920px;top:19px;width:194px;height:32px;background:var(--orange);color:var(--white);font-size:11px;padding:0 10px;display:flex;align-items:center;justify-content:space-between}
.intro{position:absolute;left:0;top:152px;width:1200px;text-align:center}
.intro h1{font-family:"Raleway",sans-serif;font-weight:800;font-size:22px;color:var(--blue-title);letter-spacing:.2px}
.intro p{margin:22px auto 0;width:600px;font-family:"Raleway",sans-serif;font-size:14.5px;line-height:22px;color:#555;text-align:justify;text-align-last:center}
.plan{position:absolute;background:var(--white);border:1px solid var(--line);text-align:center}
.plan-head{height:46px;display:flex;align-items:center;justify-content:center;gap:8px;color:var(--white);font-family:"Raleway",sans-serif;font-weight:800;font-size:17px}
.plan-head.orange{background:var(--orange)}
.plan-head.dark{background:var(--dark)}
.plan-head.blue{background:var(--blue)}
.plan-price{height:87px;padding-top:17px}
.plan-price .period{font-size:10px;color:#777;letter-spacing:.4px}
.plan-price .amount{font-family:"Raleway",sans-serif;font-weight:800;font-size:38px;color:var(--blue);line-height:42px}
.features{list-style:none}
.features li{height:30px;line-height:30px;font-size:10.5px;color:#444;letter-spacing:.3px}
.features li:nth-child(odd){background:var(--row-alt)}
.buy{display:inline-flex;align-items:center;gap:4px;margin-top:16px;width:128px;height:32px;justify-content:center;background:linear-gradient(#f68a3a,var(--orange-btn));border:1px solid #d85f14;border-radius:2px;color:var(--white);font-size:12px;font-weight:600}
.plan.featured{box-shadow:0 2px 8px rgba(0,0,0,.18);z-index:2;border:none}
.plan.featured .plan-head{height:57px;font-size:18px}
.plan.featured .plan-price{height:100px;padding-top:22px}
.plan.featured .plan-price .period{font-size:12px}
.plan.featured .plan-price .amount{font-size:42px;line-height:46px}
.plan.featured .features li{height:29.8px;line-height:30px}
.plan.featured .buy{margin-top:20px}
.footer{position:absolute;left:0;top:798px;width:1200px;height:280px;background:var(--footer)}
.fcol{position:absolute;top:34px;color:var(--white);font-family:"Raleway",sans-serif}
.fcol h3{font-weight:700;font-size:18px;letter-spacing:.3px;padding-bottom:8px;position:relative;width:133px}
.fcol h3::after{content:"";position:absolute;left:0;bottom:0;width:133px;height:1px;background:rgba(255,255,255,.35)}
.fcol h3::before{content:"";position:absolute;left:0;bottom:0;width:40px;height:2px;background:var(--orange-btn);z-index:1}
.fcol p{font-size:14px;line-height:18px;margin-top:26px}
.fcol .meta{font-size:13px;margin-top:8px;display:flex;align-items:center;gap:8px}
.newsletter{display:flex;margin-top:18px;width:214px;height:32px}
.newsletter .field{flex:1;background:var(--white);color:#333;font-size:12px;font-weight:600;display:flex;align-items:center;padding-left:10px;font-family:"Open Sans",sans-serif}
.newsletter .go{width:65px;background:var(--orange-btn);display:flex;align-items:center;justify-content:center;font-size:12px;font-weight:700}
.divider{position:absolute;top:80px;width:1px;height:180px;background:rgba(255,255,255,.06)}
.contact-line{display:flex;align-items:center;gap:8px;font-size:13px;margin-top:20px}
.fcol .socials{margin-top:26px;gap:13px}
.base{position:absolute;left:0;top:1078px;width:1200px;height:53px;background:var(--footer-base);color:var(--white);font-family:"Raleway",sans-serif;font-size:14.5px}
.base .copy{position:absolute;left:95px;top:18px}
.base .links{position:absolute;right:100px;top:18px;display:flex;gap:18px}
</style>
</head>
<body>

<header>
  <div class="topbar">
    <div class="contact">
      <span><svg width="8" height="12" viewBox="0 0 8 12"><path d="M2 1 L4 1 L4.5 3.5 L3 4.5 Q4 7.5 5.5 8.5 L7 7.5 L7.5 10 L6 11 Q1.5 9 1 3 Z" fill="#fff"/></svg>Call Us: (555)-208-1937</span>
      <span style="margin-left:6px"><svg width="18" height="12" viewBox="0 0 18 12"><rect x="1" y="1" width="16" height="10" fill="none" stroke="#fff" stroke-width="1.2"/><path d="M1 1 L9 7 L17 1" fill="none" stroke="#fff" stroke-width="1.2"/></svg>Mail: info@example.com</span>
    </div>
    <div class="socials"><i class="dot"></i><i class="dot"></i><i class="dot"></i><i class="dot"></i><i class="dot"></i><i class="dot"></i><i class="dot"></i></div>
  </div>
  <nav class="navbar">
    <div class="brand"><span class="brand-mark"></span><span class="brand-name">tallyroost</span></div>
    <ul class="menu"><li>Home</li><li>Pages</li><li>Features</li><li>Portfolio</li><li>Admintheme</li><li>Blog</li><li>Contact</li></ul>
    <div class="search"><span>Search</span><svg width="13" height="13" viewBox="0 0 13 13"><circle cx="7.5" cy="5.5" r="4" fill="none" stroke="#fff" stroke-width="1.3"/><path d="M4.6 8.4 L1 12" stroke="#fff" stroke-width="1.4"/></svg></div>
  </nav>
</header>

<main>
  <section class="intro">
    <h1>CHOSE YOUR PLAN</h1>
    <p>Lorem ipsum dolor sit amet, consectetuer adipiscing elit, sed diam nonummy nibh euismod tincidunt ut laoreet dolore magna aliquam erat volutpat.</p>
  </section>

  <article class="plan" style="left:184px;top:313px;width:207px;height:404px">
    <div class="plan-head orange"><svg width="18" height="18" viewBox="0 0 18 18"><path d="M9 1 L17 1 L17 9 L8 17 L1 10 Z" fill="#fff"/><circle cx="13" cy="5" r="1.6" fill="#f7941d"/></svg>BASIC</div>
    <div class="plan-price"><div class="period">MONTHLY</div><div class="amount">$50</div></div>
    <ul class="features"><li>50 GB Storage</li><li>Unlimited Bandwith</li><li>Domain 1</li><li>Unlimited Email accounts</li><li>Database 1</li><li>Unlimited Accounts</li><li>No Support</li></ul>
    <div class="buy"><svg width="14" height="12" viewBox="0 0 14 12"><path d="M0 1 L3 1 L4.5 8 L12 8 L13.5 3 L3.5 3" fill="#fff"/><circle cx="5.5" cy="10.5" r="1.3" fill="#fff"/><circle cx="11" cy="10.5" r="1.3" fill="#fff"/></svg>Buy Your Plan</div>
  </article>

  <article class="plan featured" style="left:391px;top:294px;width:212px;height:439px">
    <div class="plan-head blue"><svg width="36" height="26" viewBox="0 0 36 26"><path d="M1 6 L8 3 L13 5 L20 2 L27 4 L35 2 L35 14 L30 16 L22 23 Q19 25 16 22 L7 15 L1 15 Z" fill="#fff"/><path d="M13 8 L19 12 L24 8" fill="none" stroke="#0355a3" stroke-width="1.5"/></svg>STANDERD</div>
    <div class="plan-price"><div class="period">MONTHLY</div><div class="amount">$60</div></div>
    <ul class="features"><li>100 GB Storage</li><li>Unlimited Bandwith</li><li>Domain 10</li><li>Unlimited Email accounts</li><li>Database10</li><li>Unlimited Accounts</li><li>7*24 Support</li></ul>
    <div class="buy"><svg width="14" height="12" viewBox="0 0 14 12"><path d="M0 1 L3 1 L4.5 8 L12 8 L13.5 3 L3.5 3" fill="#fff"/><circle cx="5.5" cy="10.5" r="1.3" fill="#fff"/><circle cx="11" cy="10.5" r="1.3" fill="#fff"/></svg>Buy Your Plan</div>
  </article>

  <article class="plan" style="left:602px;top:313px;width:206px;height:404px">
    <div class="plan-head dark"><svg width="26" height="20" viewBox="0 0 26 20"><path d="M2 5 L7 11 L13 3 L19 11 L24 5 L22 15 L4 15 Z" fill="#fff"/><rect x="4" y="16" width="18" height="3" fill="#fff"/></svg>PREMIUM</div>
    <div class="plan-price"><div class="period">MONTHLY</div><div class="amount">$70</div></div>
    <ul class="features"><li>1TB Storage</li><li>Unlimited Bandwith</li><li>Ultimited Domains</li><li>Unlimited Email accounts</li><li>Ultimited Databases</li><li>Unlimited Accounts</li><li>7*24 Support</li></ul>
    <div class="buy"><svg width="14" height="12" viewBox="0 0 14 12"><path d="M0 1 L3 1 L4.5 8 L12 8 L13.5 3 L3.5 3" fill="#fff"/><circle cx="5.5" cy="10.5" r="1.3" fill="#fff"/><circle cx="11" cy="10.5" r="1.3" fill="#fff"/></svg>Buy Your Plan</div>
  </article>

  <article class="plan" style="left:807px;top:313px;width:208px;height:404px">
    <div class="plan-head orange"><svg width="22" height="18" viewBox="0 0 22 18"><rect x="1" y="4" width="20" height="13" rx="1" fill="#fff"/><rect x="7" y="1" width="8" height="4" fill="none" stroke="#fff" stroke-width="1.5"/><rect x="9" y="9" width="4" height="3" fill="#f7941d"/></svg>PROFESSIONAL</div>
    <div class="plan-price"><div class="period">MONTHLY</div><div class="amount">$150</div></div>
    <ul class="features"><li>3TB Storage</li><li>Unlimited Bandwith</li><li>Ultimited Domains</li><li>Unlimited Email accounts</li><li>Ultimited Databases</li><li>Unlimited Accounts</li><li>7*24 Support</li></ul>
    <div class="buy"><svg width="14" height="12" viewBox="0 0 14 12"><path d="M0 1 L3 1 L4.5 8 L12 8 L13.5 3 L3.5 3" fill="#fff"/><circle cx="5.5" cy="10.5" r="1.3" fill="#fff"/><circle cx="11" cy="10.5" r="1.3" fill="#fff"/></svg>Buy Your Plan</div>
  </article>
</main>

<footer>
  <div class="footer">
    <span class="divider" style="left:330px"></span>
    <span class="divider" style="left:592px"></span>
    <span class="divider" style="left:880px"></span>

    <div class="fcol" style="left:92px">
      <h3>Newsletter</h3>
      <p style="width:210px">Lorem ipsum dolor sit amet, consectetuer adipiscing elit, sed nonummy nibh volutpat.</p>
      <div class="newsletter"><span class="field">Email Address</span><span class="go">GO !</span></div>
    </div>

    <div class="fcol" style="left:353px">
      <h3>Latest Tweet</h3>
      <p style="width:215px;text-indent:24px">Lorem ipsum dolor sit amet, consectetuer adipiscing elit, sed nonummy nibh volutpat.</p>
      <div class="meta"><svg width="14" height="13" viewBox="0 0 14 13"><rect x="1" y="2" width="12" height="10" fill="none" stroke="#f37122" stroke-width="1.3"/><rect x="1" y="2" width="12" height="3" fill="#f37122"/></svg>28 Feb 2016</div>
      <p style="width:215px;text-indent:24px;margin-top:18px">Lorem ipsum dolor sit amet, consectetuer adipiscing elit, sed nonummy nibh volutpat.</p>
      <div class="meta"><svg width="14" height="13" viewBox="0 0 14 13"><rect x="1" y="2" width="12" height="10" fill="none" stroke="#f37122" stroke-width="1.3"/><rect x="1" y="2" width="12" height="3" fill="#f37122"/></svg>28 Feb 2016</div>
    </div>

    <div class="fcol" style="left:615px;top:32px">
      <h3>Latest Blog</h3>
      <p style="width:215px;line-height:22px;margin-top:24px">Lorem ipsum dolor sit amet, consectetuer</p>
      <div class="meta"><svg width="14" height="13" viewBox="0 0 14 13"><rect x="1" y="2" width="12" height="10" fill="none" stroke="#f37122" stroke-width="1.3"/><rect x="1" y="2" width="12" height="3" fill="#f37122"/></svg>05-02-16</div>
      <div class="meta" style="margin-top:10px;font-size:12.5px"><svg width="12" height="12" viewBox="0 0 12 12"><circle cx="6" cy="4" r="3" fill="#f37122"/><path d="M0 12 Q6 5 12 12 Z" fill="#f37122"/></svg>By Dana Whitlow<svg style="margin-left:14px" width="20" height="14" viewBox="0 0 20 14"><ellipse cx="8" cy="6" rx="7" ry="5" fill="none" stroke="#f37122" stroke-width="1.5"/><path d="M4 10 L3 13 L7 11" fill="#f37122"/></svg>05 Comments</div>
    </div>

    <div class="fcol" style="left:931px">
      <h3>Contact Us</h3>
      <div class="contact-line" style="margin-top:26px"><svg width="16" height="16" viewBox="0 0 16 16"><circle cx="8" cy="8" r="7" fill="none" stroke="#f37122" stroke-width="1.3"/><path d="M5.5 4 L7 4 L7.3 6 L6.3 6.6 Q7 8.5 8.8 9.6 L9.8 8.8 L11.6 9.4 L11.4 11 Q5 10.5 5.5 4 Z" fill="#f37122"/></svg>1-555-300-18274</div>
      <div class="contact-line" style="font-size:14px"><svg width="12" height="16" viewBox="0 0 12 16"><path d="M6 1 Q11 1 11 6 Q11 9 6 15 Q1 9 1 6 Q1 1 6 1 Z" fill="#f37122"/><circle cx="6" cy="6" r="2" fill="#0b4f96"/></svg>2290 Maple Ln, Brookvale</div>
      <div class="socials"><i class="dot"></i><i class="dot"></i><i class="dot"></i><i class="dot"></i><i class="dot"></i><i class="dot"></i></div>
    </div>
  </div>
  <div class="base">
    <span class="copy">Powered by Nordvane. All Rights Reserved.</span>
    <div class="links"><span>FAQ's</span><span>Sitemap</span><span>Contact</span></div>
  </div>
</footer>

</body>
</html>
```